Website for Construction Company
Fire, Water, Mold, Storm
Project: Website for Construction Company
Website for Construction Company - Construction
Creative Brief
Construction
www.harborlinebuilders.com
Kestrel Ridge Builders has over 20 years experience in the construction business. Our company has a variety of experienced workers and subcontractors that provide services for banks, insurance companies, lenders, real estate agents, investors, and homeowners.Our services include, Fire Damage Restoration, Water Damage Restoration, Mold Remediation, Storm Damage Restoration, Smoke Damage Restoration, Vandalism Restoration, Remodeling, and home additions. REO services include, boarding/securing properties, Re-keying, clean out/trashouts, Property Inspections,Property winterizations etc.
I would like to see the Chatterloop, Work Weave, and Quippr links. NTA logo, orba, tollipay, coastal transfer, and wayfarer Credit cards accepted. We are licensed, bonded and insured. I would like to have client testimonials, request for free estimates,
Red
Green, Yellow
left side
http://www.quillmere-renewal.com/
http://www.hearthmend.com/
http://www.tamsenfold.com/
http://www.ok-revivals.com http://www.zelvamend.com/

```html
<!DOCTYPE html>
<html lang="en">
<head>
<meta charset="utf-8">
<title>Kestrel Ridge Builders – Home Restoration Specialists</title>
<link rel="stylesheet" href="https://fonts.googleapis.com/css2?family=Arimo:wght@400;700&display=swap">
<style>
  :root {
    --blue-deep: #0d5fa8;
    --blue-mid: #2b86cf;
    --blue-light: #5fb0ea;
    --blue-text: #1a6cb5;
    --green: #7cc21d;
    --green-dark: #4f8f0c;
    --green-light: #a6dc3c;
    --ink: #333c44;
    --muted: #6b747c;
    --page: #ffffff;
    --band: #eef1f3;
    --footer: #cfe6f6;
    --footer-line: #b7d6ec;
    --bottom: #e3f0f9;
  }
  * { margin: 0; padding: 0; box-sizing: border-box; }
  html, body { width: 1200px; height: 1104px; overflow: hidden; }
  body { background: var(--page); font-family: "Arimo", Arial, sans-serif; color: var(--ink); position: relative; }

  .site-header { position: absolute; top: 0; left: 0; width: 1200px; height: 114px; background: var(--page); }
  .brand { position: absolute; left: 176px; top: 42px; display: flex; align-items: center; gap: 10px; }
  .brand-square { width: 40px; height: 40px; background: var(--blue-deep); border-radius: 4px; }
  .brand-name { font-size: 22px; font-weight: 700; color: var(--blue-deep); line-height: 1; }
  .brand-tag { font-size: 11px; color: var(--muted); margin-top: 4px; letter-spacing: .5px; }

  .social { position: absolute; right: 170px; top: 16px; display: flex; gap: 10px; font-size: 10px; color: var(--blue-deep); }
  .social span { display: flex; align-items: center; gap: 4px; }
  .social i { width: 10px; height: 10px; background: var(--blue-mid); display: block; }

  .main-nav { position: absolute; right: 162px; top: 66px; display: flex; gap: 4px; }
  .main-nav a { display: block; padding: 8px 13px; font-size: 12px; color: #fff; text-decoration: none;
    background: linear-gradient(var(--green-light), var(--green-dark)); border-radius: 4px 4px 0 0; }

  .hero { position: absolute; top: 114px; left: 0; width: 1200px; height: 322px;
    background: radial-gradient(ellipse at 60% 55%, var(--blue-light) 0%, var(--blue-mid) 40%, var(--blue-deep) 100%); overflow: hidden; }
  .hero-title { position: absolute; left: 210px; top: 130px; font-size: 40px; font-weight: 700; letter-spacing: 2px; color: rgba(255,255,255,.35); }
  .hero-copy { position: absolute; left: 212px; top: 182px; width: 330px; font-size: 12px; line-height: 1.45; color: #fff; }
  .hero-button { position: absolute; left: 212px; top: 250px; padding: 8px 16px; font-size: 12px; color: #fff;
    border: 1px solid rgba(255,255,255,.7); border-radius: 4px; background: rgba(255,255,255,.12); }
  .hero-visual { position: absolute; left: 600px; top: 40px; width: 340px; height: 250px;
    background: radial-gradient(ellipse at center, rgba(255,255,255,.28) 0%, rgba(255,255,255,.08) 60%, rgba(255,255,255,0) 100%); }
  .hero-dots { position: absolute; left: 540px; top: 306px; display: flex; gap: 6px; }
  .hero-dots i { width: 24px; height: 5px; background: rgba(255,255,255,.5); display: block; }
  .hero-dots i.active { background: var(--green); }

  .services { position: absolute; top: 436px; left: 0; width: 1200px; height: 318px; background: var(--band); }
  .services-arrow { position: absolute; top: 120px; }
  .services-arrow.prev { left: 150px; }
  .services-arrow.next { left: 1094px; }
  .service { position: absolute; top: 30px; width: 226px; text-align: center; }
  .service-photo { width: 226px; height: 226px; border-radius: 50%; border: 9px solid var(--green);
    box-shadow: 0 0 0 3px var(--green-dark) inset, 0 2px 6px rgba(0,0,0,.2); }
  .service-label { margin: -16px auto 0; position: relative; width: 200px; padding: 5px 0; font-size: 13px; font-weight: 700;
    color: var(--ink); background: linear-gradient(var(--green-light), var(--green)); border-radius: 3px; }

  .welcome { position: absolute; top: 766px; left: 176px; width: 360px; }
  .welcome h1 { font-size: 20px; color: var(--blue-text); font-weight: 700; margin-bottom: 10px; }
  .welcome p { font-size: 10px; line-height: 1.45; color: var(--muted); }
  .read-more { display: block; text-align: right; font-size: 10px; color: var(--ink); margin-top: 4px; text-decoration: none; }

  .testimonial { position: absolute; top: 770px; left: 556px; width: 350px; padding: 14px 16px 20px 30px; border: 1px solid #dde2e6;
    border-radius: 6px; font-size: 10.5px; line-height: 1.5; color: var(--muted); }
  .testimonial svg { position: absolute; left: 10px; top: 14px; }
  .testimonial-author { position: absolute; right: 90px; bottom: -10px; background: #fff; border: 1px solid #dde2e6; border-radius: 10px;
    padding: 2px 10px; font-size: 9.5px; color: var(--ink); }
  .testimonial-photo { position: absolute; left: 910px; top: 750px; width: 128px; height: 190px;
    background: linear-gradient(#f2f2f2, #c9ccd0 60%, #8d949b); }

  .site-footer { position: absolute; top: 946px; left: 0; width: 1200px; height: 100px; background: var(--footer); border-top: 1px solid var(--footer-line); }
  .footer-col { position: absolute; top: 10px; width: 200px; font-size: 10px; line-height: 1.4; color: var(--muted); }
  .footer-col h2 { font-size: 11px; color: var(--blue-deep); margin-bottom: 4px; }
  .footer-col strong { color: var(--ink); }
  .cards { position: absolute; left: 868px; top: 10px; width: 220px; }
  .cards h2 { font-size: 11px; color: var(--blue-deep); margin-bottom: 6px; }
  .cards ul { list-style: none; display: grid; grid-template-columns: 90px 120px; gap: 6px 8px; }
  .cards li { display: flex; align-items: center; gap: 5px; font-size: 10px; color: var(--ink); white-space: nowrap; }
  .cards li i { width: 12px; height: 12px; background: #fff; border: 1px solid var(--footer-line); display: block; }

  .bottom-bar { position: absolute; top: 1046px; left: 0; width: 1200px; height: 58px; background: var(--bottom); }
  .bottom-links { position: absolute; left: 176px; top: 12px; font-size: 10px; color: var(--ink); }
  .copyright { position: absolute; left: 176px; top: 30px; font-size: 9.5px; color: var(--muted); }
  .badge { position: absolute; left: 1004px; top: 8px; width: 30px; height: 42px; background: var(--blue-deep); border-radius: 3px; }
</style>
</head>
<body>
  <header class="site-header">
    <div class="brand">
      <div class="brand-square"></div>
      <div>
        <div class="brand-name">Kestrel Ridge Builders</div>
        <div class="brand-tag">Home Restoration Specialists</div>
      </div>
    </div>
    <div class="social">
      <span><i></i>Chatterloop</span>
      <span><i></i>Work Weave</span>
      <span><i></i>Quippr</span>
    </div>
    <nav class="main-nav">
      <a href="#">Home</a><a href="#">About Us</a><a href="#">Services</a><a href="#">Industry</a><a href="#">Photogallery</a><a href="#">News</a><a href="#">Contact Us</a>
    </nav>
  </header>

  <section class="hero">
    <div class="hero-title">LOREM IPSUM IS</div>
    <p class="hero-copy">Lorem Ipsum is simply dummy text of the printing and typesetting industry. Lorem Ipsum has been the industry's standard dummy text ever since the 1500s.</p>
    <div class="hero-button">Contact Us Today</div>
    <div class="hero-visual" role="img" aria-label="A model house resting on an open hand"></div>
    <div class="hero-dots"><i class="active"></i><i></i><i></i><i></i></div>
  </section>

  <section class="services">
    <svg class="services-arrow prev" width="20" height="60" viewBox="0 0 20 60"><path d="M16 4 L4 30 L16 56" fill="none" stroke="#9aa3ab" stroke-width="3"/></svg>
    <svg class="services-arrow next" width="20" height="60" viewBox="0 0 20 60"><path d="M4 4 L16 30 L4 56" fill="none" stroke="#9aa3ab" stroke-width="3"/></svg>
    <div class="service" style="left:172px">
      <div class="service-photo" role="img" aria-label="Smoke damaged house" style="background:linear-gradient(#9fb7c9,#5f7f95)"></div>
      <div class="service-label">Smoke Damage Restoration</div>
    </div>
    <div class="service" style="left:403px">
      <div class="service-photo" role="img" aria-label="House damaged by fire" style="background:linear-gradient(#8a6a55,#3d2c24)"></div>
      <div class="service-label">Fire Damage Restoration</div>
    </div>
    <div class="service" style="left:631px">
      <div class="service-photo" role="img" aria-label="Water damaged wall" style="background:linear-gradient(#a9a294,#6e675c)"></div>
      <div class="service-label">Water Damage Restoration</div>
    </div>
    <div class="service" style="left:853px">
      <div class="service-photo" role="img" aria-label="Storm damaged building" style="background:linear-gradient(#b7b3a8,#6f6a60)"></div>
      <div class="service-label">Storm Damage Restoration</div>
    </div>
  </section>

  <section class="welcome">
    <h1>Welcome to Kestrel Ridge Builders</h1>
    <p>Lorem Ipsum is simply dummy text of the printing and typesetting industry. Lorem Ipsum has been the industry's standard dummy text ever since the 1500s, when an unknown printer took a galley of type and scrambled it to make a type specimen book. It has survived not only five centuries, but also the leap into electronic typesetting, remaining essentially unchanged. It was popularised in the 1960s with the release of Letraset sheets containing Lorem Ipsum passages, and more recently with desktop publishing software.</p>
    <a class="read-more" href="#">Read more »</a>
  </section>

  <aside class="testimonial">
    <svg width="12" height="10" viewBox="0 0 12 10"><path d="M0 10V5L3 0h2L3 5h2v5zM7 10V5l3-5h2l-2 5h2v5z" fill="#9aa3ab"/></svg>
    Lorem Ipsum is simply dummy text of the printing and typesetting industry. Lorem Ipsum has been the industry's standard dummy text ever since the 1500s, when an unknown printer took a galley of type and scrambled it to make a type specimen book. It has survived not only five centuries, but also the leap into electronic typesetting remaining essentially unchanged.
    <span class="testimonial-author">Lorem Ipsum</span>
  </aside>
  <div class="testimonial-photo" role="img" aria-label="Family of homeowners"></div>

  <footer class="site-footer">
    <div class="footer-col" style="left:176px">
      <h2>Location</h2>
      Lorem Ipsum is simply dummy text of the printing and typesetting industry. Lorem Ipsum has been the industry's standard.
    </div>
    <div class="footer-col" style="left:400px">
      <h2>Contact</h2>
      <strong>Toll free</strong> (555) 014-2290<br>
      <strong>Phone</strong> (555) 014-2291<br>
      <strong>Fax</strong> (555) 014-2292<br>
      <strong>Email</strong> hello@kestrelridge.example
    </div>
    <div class="footer-col" style="left:624px">
      <h2>Licensed</h2>
      Lorem Ipsum is simply dummy text of the printing and typesetting industry. Lorem Ipsum has been the standard.
    </div>
    <div class="cards">
      <h2>Cards Accepted</h2>
      <ul>
        <li><i></i>wayfarer</li>
        <li><i></i>tollipay</li>
        <li><i></i>orba</li>
        <li><i></i>coastal transfer</li>
      </ul>
    </div>
  </footer>

  <div class="bottom-bar">
    <div class="bottom-links">About Us | Services | Industry | Photogallery | News | Contact Us</div>
    <div class="copyright">Copyright © 2012 Kestrel Ridge Builders. All Rights Reserved</div>
    <div class="badge"></div>
  </div>
</body>
</html>
```